SHOPIFY Store Website- complete design and functionality

I am looking for someone to create a modern and clean looking e-commerce store for our new holiday lighting and decor distribution company through Shopify. We will have a variety of products - greenery (wreaths, garland by size), bows, lighting (different types of lighting - c9 bulbs in various colors, 5mm mini lights, c7) and a variety of accessories needed to install your own lighting and decor.

Need to be complete- ready to use.
thx
Updates

We want a fully functional design including set up on Shopify. Assuming we can give you our Shopify password to get it all set up? Have never done this. Please let us know how it works and what an estimated cost would be or what other details you need to provide pricing estimate. thanks

Target Market(s)

Lighting

Font styles to use
Serif
Sans Serif

Requirements
Must have
• A clean and easy to use interface. We have a shopping cart listed on Shopify already. We would like the website to match our company logo as well.

```html
<!DOCTYPE html>
<html lang="en">
<head>
<meta charset="utf-8">
<title>Brightwell Lights – Holiday Lighting &amp; Decor</title>
<link href="https://fonts.googleapis.com/css2?family=Poppins:wght@400;500;600;700&family=Roboto:wght@400;500;700&family=Kaushan+Script&display=swap" rel="stylesheet">
<style>
:root{
  --blue:#0b6fc4;
  --blue-dark:#0a4f9a;
  --navy:#0d2a6e;
  --orange:#f7941d;
  --orange-dark:#e5800a;
  --ink:#222;
  --muted:#666;
  --line:#e4e4e4;
  --light:#f5f5f5;
  --black:#0b0b0b;
  --star:#f5b301;
}
*{box-sizing:border-box;margin:0;padding:0}
html,body{width:1200px;height:4950px;overflow:hidden}
body{position:relative;font-family:"Roboto",Arial,sans-serif;color:var(--ink);background:#fff}
.section{position:absolute;left:0;width:1200px}
.ph{display:block}
a{color:inherit;text-decoration:none}

/* header */
.header{top:0;height:92px;background:#fff;border-bottom:1px solid var(--line)}
.brand{position:absolute;left:98px;top:18px;display:flex;align-items:center;gap:10px}
.brand-name{font-family:"Poppins",sans-serif;font-weight:700;font-size:36px;color:var(--blue);letter-spacing:.5px}
.brand-dot{width:14px;height:14px;background:var(--orange);border-radius:50%}
.topbar{position:absolute;right:0;top:0;height:40px;width:650px;background:var(--blue);clip-path:polygon(26px 0,100% 0,100% 100%,0 100%);display:flex;align-items:center;justify-content:flex-end;gap:22px;padding-right:50px;color:#fff;font-size:14px}
.topbar span{display:flex;align-items:center;gap:6px}
.lang{border:1px solid #fff;padding:2px 8px;border-radius:3px}
.nav{position:absolute;right:105px;top:58px;display:flex;gap:27px;font-family:"Poppins",sans-serif;font-size:13px;font-weight:500;text-transform:uppercase;align-items:center}
.nav-icons{display:flex;gap:18px;margin-left:6px}

/* hero */
.hero{top:92px;height:475px;background:linear-gradient(115deg,#1c7fd0,#0a5cab);overflow:hidden}
.hero-photo{position:absolute;right:0;top:0;width:720px;height:475px;clip-path:polygon(140px 0,100% 0,100% 100%,0 100%);background:radial-gradient(circle at 60% 40%,#c69a6a,#5a3b28 55%,#1f1714)}
.hero-edge{position:absolute;right:0;top:0;width:738px;height:475px;clip-path:polygon(140px 0,158px 0,18px 100%,0 100%);background:var(--orange)}
.hero-copy{position:absolute;left:100px;top:120px;color:#fff;width:380px;text-align:center}
.hero-kicker{font-family:"Poppins",sans-serif;font-size:18px;text-align:left;white-space:nowrap}
.hero-deal{font-family:"Kaushan Script",cursive;font-size:92px;line-height:1.1;margin-top:8px}
.hero-sub{font-family:"Poppins",sans-serif;font-size:38px;font-weight:500;margin-top:-4px}
.btn-solid{display:inline-block;background:var(--orange);color:#fff;font-family:"Poppins",sans-serif;font-weight:600;font-size:14px;text-transform:uppercase;border-radius:30px;padding:14px 38px}
.hero .btn-solid{margin-top:26px}
.hero-arrow{position:absolute;top:225px;color:#fff;font-size:30px}
.dots{position:absolute;display:flex;gap:7px}
.dots i{width:10px;height:10px;border:1.5px solid #fff;border-radius:50%}
.dots i.on{background:#fff}

/* features */
.features{top:567px;height:88px;background:var(--light);display:flex;justify-content:center}
.feature{width:315px;display:flex;align-items:center;gap:18px;padding-left:60px;border-right:1px solid var(--line)}
.feature:last-child{border:none}
.feature h4{font-family:"Poppins",sans-serif;font-size:14px;font-weight:600}
.feature p{font-size:12px;color:#444;line-height:1.35}

/* categories */
.cats{top:720px;height:490px}
.cat{position:absolute;overflow:hidden}
.cat-label{position:absolute;font-family:"Poppins",sans-serif;font-weight:600;font-size:25px;color:#222}
.cat .btn-solid{position:absolute;padding:12px 34px;font-size:13px}

/* product grids */
.heading{font-family:"Poppins",sans-serif;font-weight:600;font-size:38px;text-transform:uppercase;color:#111}
.products-title{top:1270px;text-align:center}
.grid{position:absolute;left:104px;display:flex;gap:22px}
.card{width:232px;background:#fff;box-shadow:0 2px 10px rgba(0,0,0,.08);padding-bottom:16px}
.card .ph{width:232px;height:206px}
.card-body{padding:18px 12px 0}
.stars{display:flex;align-items:center;gap:8px;font-size:11px}
.stars b{color:var(--star);letter-spacing:1px;font-size:14px}
.stars u{color:#555}
.card h5{font-size:15px;font-weight:500;line-height:1.4;margin-top:12px}
.price{font-size:17px;font-weight:500;margin-top:12px}
.btn-line{display:block;border:1.5px solid var(--orange);color:var(--orange);border-radius:24px;text-align:center;font-family:"Poppins",sans-serif;font-size:13px;font-weight:500;padding:9px 0;margin-top:18px;text-transform:uppercase}

/* offer */
.offer{top:2262px;height:378px;background:radial-gradient(ellipse at 55% 50%,#1b47a8,#0d2a6e 70%)}
.offer-deco{position:absolute;top:0;height:378px}
.offer-copy{position:absolute;left:340px;width:620px;top:62px;text-align:center;color:#fff}
.offer-copy h3{font-family:"Poppins",sans-serif;font-weight:700;font-size:46px}
.offer-script{font-family:"Kaushan Script",cursive;font-size:52px;margin-top:2px;line-height:1.2}
.offer-copy p{font-family:"Poppins",sans-serif;font-size:15px;margin-top:6px}
.btn-ghost{display:inline-block;border:1.5px solid #fff;color:#fff;padding:11px 26px;font-family:"Poppins",sans-serif;font-size:15px;font-weight:500;margin-top:28px;border-radius:3px}

/* decorations */
.deco-head{position:absolute;left:128px;top:2730px;width:940px;display:flex;align-items:center;gap:18px}
.deco-head .rule{flex:1;height:1px;background:var(--line)}
.arrows{display:flex;gap:10px}
.arrows i{width:36px;height:36px;border-radius:50%;box-shadow:0 1px 6px rgba(0,0,0,.18);display:flex;align-items:center;justify-content:center;font-style:normal;font-size:18px}

/* testimonials */
.testi{top:3300px;height:470px;background:linear-gradient(180deg,#1d6fc0,#0c5aab)}
.testi h2{position:absolute;top:100px;width:100%;text-align:center;color:#fff;font-family:"Poppins",sans-serif;font-weight:600;font-size:38px}
.quote{position:absolute;top:183px;width:428px;height:180px;background:#fff;padding:26px 40px 0 42px}
.quote p{font-style:italic;font-size:14px;line-height:1.8;color:#222}
.quote b{display:block;font-size:15px;margin-top:10px}
.qmark{position:absolute;left:-28px;top:62px;width:56px;height:56px;border-radius:50%;background:var(--orange);color:#fff;font-family:"Poppins",sans-serif;font-size:50px;font-weight:700;text-align:center;line-height:76px}
.testi .hero-arrow{top:250px}

/* blog */
.blog-title{top:3855px;text-align:center}
.blog{position:absolute;top:3928px;width:325px}
.blog .ph{width:325px;height:205px}
.blog h5{font-size:16px;font-weight:500;line-height:1.45;margin-top:18px}
.blog p{font-size:11.5px;color:#555;line-height:1.65;margin-top:10px}
.more{display:block;color:var(--orange);font-size:12px;font-weight:500;margin-top:16px}

/* newsletter */
.news{top:4380px;height:175px;background:var(--blue)}
.news h3{position:absolute;left:97px;top:62px;color:#fff;font-family:"Poppins",sans-serif;font-weight:600;font-size:24px}
.news p{position:absolute;left:97px;top:104px;color:#fff;font-size:13px}
.news-form{position:absolute;left:572px;top:57px;width:562px;height:62px;background:#fff;border-radius:31px;display:flex;align-items:center;justify-content:space-between;padding-left:28px;font-size:13px;color:#888}
.news-form span.btn-solid{height:62px;line-height:34px;padding:14px 40px;font-size:16px}

/* footer */
.footer{top:4555px;height:395px;background:var(--black);color:#fff}
.fcol{position:absolute;top:72px}
.fcol h6{font-family:"Poppins",sans-serif;font-weight:500;font-size:17px;text-transform:uppercase;margin-bottom:18px}
.fcol li{list-style:none;font-size:13px;line-height:29px}
.fcol p{font-size:13px;line-height:29px}
.femail{display:flex;justify-content:space-between;align-items:center;width:205px;height:36px;border-radius:18px;background:#fff;color:#777;font-size:12px;padding:0 4px 0 14px;margin-top:10px}
.femail i{width:30px;height:30px;border-radius:50%;background:var(--orange)}
.social{display:flex;gap:12px;margin-top:20px}
.social i{width:40px;height:40px;border:1.5px solid #fff;border-radius:50%}
.copy{position:absolute;left:120px;top:357px;font-size:12.5px}
.pay{position:absolute;right:96px;top:350px;display:flex;gap:14px;align-items:center}
.pay span{font-family:"Roboto",sans-serif;font-weight:500;font-size:12px;color:#fff;display:flex;align-items:center;gap:5px}
.pay span i{width:10px;height:10px;background:#fff;display:inline-block}
</style>
</head>
<body>

<header class="section header">
  <div class="brand"><span class="brand-name">BRIGHTWELL</span><span class="brand-dot"></span></div>
  <div class="topbar">
    <span><svg width="16" height="12" viewBox="0 0 16 12"><rect x="1" y="1" width="14" height="10" fill="none" stroke="#fff" stroke-width="1.4"/><path d="M1 1l7 6 7-6" fill="none" stroke="#fff" stroke-width="1.4"/></svg>info@brightwelllights.com</span>
    <span><svg width="14" height="14" viewBox="0 0 14 14"><path d="M3 1l2 3-1.5 1.5a8 8 0 004 4L9 8l3 2-1 3C6 13 1 8 1 3z" fill="none" stroke="#fff" stroke-width="1.3"/></svg>+1 555 010 2040</span>
    <span><svg width="13" height="14" viewBox="0 0 13 14"><circle cx="6.5" cy="4" r="3" fill="none" stroke="#fff" stroke-width="1.3"/><path d="M1 13a5.5 5 0 0111 0" fill="none" stroke="#fff" stroke-width="1.3"/></svg>Sign in</span>
    <span class="lang">En ▾</span>
  </div>
  <nav class="nav">
    <a>Home</a><a>New Products</a><a>Shop by Category</a><a>Clearance</a><a>Sale</a><a>Free Resources</a>
    <span class="nav-icons">
      <svg width="18" height="16" viewBox="0 0 18 16"><path d="M9 15S1 10 1 5a4 4 0 018-1 4 4 0 018 1c0 5-8 10-8 10z" fill="none" stroke="#333" stroke-width="1.4"/></svg>
      <svg width="18" height="17" viewBox="0 0 18 17"><path d="M1 1h3l2 10h9l2-7H5" fill="none" stroke="#333" stroke-width="1.4"/><circle cx="7" cy="15" r="1.3" fill="#333"/><circle cx="14" cy="15" r="1.3" fill="#333"/></svg>
    </span>
  </nav>
</header>

<section class="section hero">
  <div class="hero-edge"></div>
  <div class="hero-photo" role="img" aria-label="Woman hanging warm patio string lights at dusk"></div>
  <div class="hero-copy">
    <div class="hero-kicker">When The Sun Goes Down, the Magic Begins</div>
    <div class="hero-deal">20% Off</div>
    <div class="hero-sub">Patio Lighting</div>
    <a class="btn-solid">Shop Now</a>
  </div>
  <span class="hero-arrow" style="left:52px">‹</span>
  <span class="hero-arrow" style="right:50px">›</span>
  <div class="dots" style="left:564px;top:433px"><i class="on"></i><i></i><i></i><i></i></div>
</section>

<section class="section features">
  <div class="feature">
    <svg width="44" height="32" viewBox="0 0 44 32"><rect x="2" y="4" width="26" height="18" fill="none" stroke="#555" stroke-width="1.6"/><path d="M28 10h8l6 6v6H28z" fill="none" stroke="#555" stroke-width="1.6"/><circle cx="10" cy="26" r="3.5" fill="#fff" stroke="#555" stroke-width="1.6"/><circle cx="35" cy="26" r="3.5" fill="#fff" stroke="#555" stroke-width="1.6"/></svg>
    <div><h4>FREE SHIPPING</h4><p>Free shipping on all US<br>order or order above $200</p></div>
  </div>
  <div class="feature">
    <svg width="40" height="36" viewBox="0 0 40 36"><path d="M4 12l16-8 16 8v18H4z" fill="none" stroke="#555" stroke-width="1.6"/><path d="M4 12l16 8 16-8M20 20v14" fill="none" stroke="#555" stroke-width="1.6"/></svg>
    <div><h4>30 Days Return</h4><p>Simply return it within<br>30 days for an exchange</p></div>
  </div>
  <div class="feature">
    <svg width="40" height="34" viewBox="0 0 40 34"><rect x="2" y="6" width="30" height="20" rx="2" fill="none" stroke="#555" stroke-width="1.6"/><path d="M2 12h30" stroke="#555" stroke-width="3"/><path d="M28 20l4 10 6-6" fill="none" stroke="#555" stroke-width="1.6"/></svg>
    <div><h4>100% Payment Secure</h4><p>Simply return it within<br>30 days for an exchange</p></div>
  </div>
</section>

<section class="section cats">
  <div class="cat" style="left:104px;top:0;width:316px;height:236px;background:linear-gradient(90deg,#f2d9b0 35%,#8a5a2a 60%,#2f5b2a)" role="img" aria-label="Holiday wreath with red berries and pine cones">
    <span class="cat-label" style="left:26px;top:26px">Greenery</span>
    <a class="btn-solid" style="left:8px;top:70px">Shop Now</a>
  </div>
  <div class="cat" style="left:428px;top:0;width:316px;height:236px;background:linear-gradient(135deg,#e5eef6,#cde0ee 45%,#b83040 75%,#e6eef5)" role="img" aria-label="Red satin bows with snowflakes and candy canes">
    <span class="cat-label" style="left:62px;top:50px">Bows</span>
    <a class="btn-solid" style="left:20px;top:94px">Shop Now</a>
  </div>
  <div class="cat" style="left:104px;top:246px;width:640px;height:236px;background:linear-gradient(90deg,#f0dccb 30%,#e9d2bf)" role="img" aria-label="Electrical tape rolls, light controller and outdoor outlet timer">
    <span class="cat-label" style="left:30px;top:110px">Accessories</span>
    <a class="btn-solid" style="left:28px;top:160px">Shop Now</a>
  </div>
  <div class="cat" style="left:756px;top:0;width:340px;height:486px;background:radial-gradient(circle at 60% 75%,#3fe3a6,#0b6e4a 22%,#3b0d12 55%,#7a1a1a 80%,#231018)" role="img" aria-label="Close-up of glowing colored C9 light bulbs">
    <span class="cat-label" style="left:112px;top:106px;color:#fff;font-size:29px">Lighting</span>
    <a class="btn-solid" style="left:94px;top:166px">Shop Now</a>
  </div>
</section>

<h2 class="section heading products-title">Our Products</h2>

<div class="grid" style="top:1355px">
  <div class="card"><div class="ph" role="img" aria-label="Edison bulb string lights glowing at night" style="background:radial-gradient(circle at 50% 55%,#f0c57a,#6b4420 45%,#1c130c)"></div><div class="card-body"><div class="stars"><b>★★★★★</b><u>5 reviews</u></div><h5>The standard Lorem Ipsum passage, used since</h5><div class="price">$129.00 - $1,199.00</div><a class="btn-line">Shop Now</a></div></div>
  <div class="card"><div class="ph" role="img" aria-label="Porch railing wrapped in garland and lights" style="background:linear-gradient(135deg,#3c5a2a,#b53a2c 45%,#e9d8b0 70%,#2d4a22)"></div><div class="card-body"><div class="stars"><b>★★★★★</b><u>5 reviews</u></div><h5>The standard Lorem Ipsum passage, used since</h5><div class="price">$129.00 - $1,199.00</div><a class="btn-line">Shop Now</a></div></div>
  <div class="card"><div class="ph" role="img" aria-label="Large lit outdoor Christmas tree at dusk" style="background:linear-gradient(180deg,#274a78,#3f6aa0 40%,#c8a850 70%,#1e3550)"></div><div class="card-body"><div class="stars"><b>★★★★★</b><u>5 reviews</u></div><h5>The standard Lorem Ipsum passage, used since</h5><div class="price">$129.00 - $1,199.00</div><a class="btn-line">Shop Now</a></div></div>
  <div class="card"><div class="ph" role="img" aria-label="Outdoor dining terrace under canopy of fairy lights" style="background:radial-gradient(circle at 50% 30%,#f7d98a,#a46b2a 45%,#3a2412)"></div><div class="card-body"><div class="stars"><b>★★★★★</b><u>5 reviews</u></div><h5>The standard Lorem Ipsum passage, used since</h5><div class="price">$129.00 - $1,199.00</div><a class="btn-line">Shop Now</a></div></div>
</div>

<div class="grid" style="top:1778px">
  <div class="card"><div class="ph" role="img" aria-label="Illuminated star decorations in white and blue" style="background:linear-gradient(135deg,#e8d4b8,#c89a72 45%,#2f5fd0 75%,#1a2f7a)"></div><div class="card-body"><div class="stars"><b>★★★★★</b><u>5 reviews</u></div><h5>The standard Lorem Ipsum passage, used since</h5><div class="price">$129.00 - $1,199.00</div><a class="btn-line">Shop Now</a></div></div>
  <div class="card"><div class="ph" role="img" aria-label="Garden shrubs covered in colored mini lights" style="background:linear-gradient(160deg,#2b3a22,#4b5a33 50%,#3a2a1e)"></div><div class="card-body"><div class="stars"><b>★★★★★</b><u>5 reviews</u></div><h5>The standard Lorem Ipsum passage, used since</h5><div class="price">$129.00 - $1,199.00</div><a class="btn-line">Shop Now</a></div></div>
  <div class="card"><div class="ph" role="img" aria-label="Faceted green, red and white C9 bulbs" style="background:linear-gradient(120deg,#0f2a18,#2fa85c 35%,#d9e6e0 60%,#b32a2a 85%)"></div><div class="card-body"><div class="stars"><b>★★★★★</b><u>5 reviews</u></div><h5>The standard Lorem Ipsum passage, used since</h5><div class="price">$129.00 - $1,199.00</div><a class="btn-line">Shop Now</a></div></div>
  <div class="card"><div class="ph" role="img" aria-label="Curtain of blue and red LED lights" style="background:linear-gradient(90deg,#0a2a6a,#2a7ae0 45%,#7a1a5a 80%,#d0204a)"></div><div class="card-body"><div class="stars"><b>★★★★★</b><u>5 reviews</u></div><h5>The standard Lorem Ipsum passage, used since</h5><div class="price">$129.00 - $1,199.00</div><a class="btn-line">Shop Now</a></div></div>
</div>

<section class="section offer">
  <div class="offer-deco" role="img" aria-label="Gold gift boxes, ribbons and pine branches" style="left:0;width:300px;background:linear-gradient(90deg,#a0782f,#6a5226 50%,rgba(13,42,110,0))"></div>
  <div class="offer-deco" role="img" aria-label="Pine branches with gold ornaments" style="right:0;width:260px;background:linear-gradient(270deg,#2f4a2a,#3c5a2e 40%,rgba(13,42,110,0))"></div>
  <div class="offer-copy">
    <h3>40% Off</h3>
    <div class="offer-script">Special Offer c9 Bulbs</div>
    <p>Lorem ipsum dolor sit amet, consectetur adipiscing elit, sed do</p>
    <a class="btn-ghost">SHOP NOW</a>
  </div>
</section>

<div class="deco-head">
  <h2 class="heading">Decorations</h2><span class="rule"></span>
  <span class="arrows"><i>‹</i><i>›</i></span>
</div>

<div class="grid" style="top:2800px;left:128px">
  <div class="card"><div class="ph" role="img" aria-label="Snow-covered Christmas tree with warm lights" style="background:radial-gradient(circle at 50% 60%,#e0a84a,#33527a 50%,#1c3050)"></div><div class="card-body"><div class="stars"><b>★★★★★</b><u>5 reviews</u></div><h5>The standard Lorem Ipsum passage, used since</h5><div class="price">$129.00 - $1,199.00</div><a class="btn-line">Shop Now</a></div></div>
  <div class="card"><div class="ph" role="img" aria-label="Close-up of pine branches with mini lights" style="background:linear-gradient(160deg,#1f3a1a,#3f6a2a 50%,#1a2a12)"></div><div class="card-body"><div class="stars"><b>★★★★★</b><u>5 reviews</u></div><h5>The standard Lorem Ipsum passage, used since</h5><div class="price">$129.00 - $1,199.00</div><a class="btn-line">Shop Now</a></div></div>
  <div class="card"><div class="ph" role="img" aria-label="Candle lights in a window at night" style="background:radial-gradient(circle at 65% 60%,#f2c066,#4a3a2a 35%,#14202e)"></div><div class="card-body"><div class="stars"><b>★★★★★</b><u>5 reviews</u></div><h5>The standard Lorem Ipsum passage, used since</h5><div class="price">$129.00 - $1,199.00</div><a class="btn-line">Shop Now</a></div></div>
  <div class="card"><div class="ph" role="img" aria-label="Decorated living room with tree and fireplace" style="background:linear-gradient(135deg,#e9e4dc,#7a8a5a 45%,#b03a34 70%,#f0ece4)"></div><div class="card-body"><div class="stars"><b>★★★★★</b><u>5 reviews</u></div><h5>The standard Lorem Ipsum passage, used since</h5><div class="price">$129.00 - $1,199.00</div><a class="btn-line">Shop Now</a></div></div>
</div>

<section class="section testi">
  <h2>CLIENT TESTIMONIALS</h2>
  <div class="quote" style="left:155px"><span class="qmark">“</span><p>Lorem ipsum dolor sit amet, consectetur adipiscing elit, sed do eiusmod tempor incididunt ut lab magna aliqua. Quis ipsum suspendisse ultrices gravida. Rus commodo viverra maecenas accumsan</p><b>- ANNA MERCER</b></div>
  <div class="quote" style="left:643px"><span class="qmark">“</span><p>Lorem ipsum dolor sit amet, consectetur adipiscing elit, sed do eiusmod tempor incididunt ut lab magna aliqua. Quis ipsum suspendisse ultrices gravida. Rus commodo viverra maecenas accumsan</p><b>- ANNA MERCER</b></div>
  <span class="hero-arrow" style="left:86px">‹</span>
  <span class="hero-arrow" style="right:94px">›</span>
  <div class="dots" style="left:564px;top:392px"><i class="on" style="background:var(--orange);border-color:var(--orange)"></i><i style="background:#fff"></i><i style="background:#fff"></i><i style="background:#fff"></i><i style="background:#fff"></i></div>
</section>

<h2 class="section heading blog-title">Latest Blog</h2>

<article class="blog" style="left:100px"><div class="ph" role="img" aria-label="Lantern with candle among globe lights" style="background:radial-gradient(circle at 40% 55%,#f6d38a,#8a5a2a 40%,#1e2a44)"></div><h5>Lorem ipsum dolor sit amctetur adipiscing elit, sed do eiusmod tempor</h5><p>Lorem ipsum dolor sit amet, consectetur adipiiing elit, sed do eiusmod tempor incididunt ut labore et dolore magna aliqua. Quis ipsum suspendisse</p><a class="more">READ MORE ⟶</a></article>
<article class="blog" style="left:438px"><div class="ph" role="img" aria-label="Hanging glowing bulbs in the dark" style="background:radial-gradient(circle at 50% 50%,#9a6a32,#2a1a10 60%,#0e0a08)"></div><h5>Lorem ipsum dolor sit amctetur adipiscing elit, sed do eiusmod tempor</h5><p>Lorem ipsum dolor sit amet, consectetur adipiiing elit, sed do eiusmod tempor incididunt ut labore et dolore magna aliqua. Quis ipsum suspendisse</p><a class="more">READ MORE ⟶</a></article>
<article class="blog" style="left:775px"><div class="ph" role="img" aria-label="Outdoor wedding ceremony under string lights" style="background:linear-gradient(180deg,#2a3a6a,#5a6a9a 40%,#c8c0a8 70%,#3a3a2a)"></div><h5>Lorem ipsum dolor sit amctetur adipiscing elit, sed do eiusmod tempor</h5><p>Lorem ipsum dolor sit amet, consectetur adipiiing elit, sed do eiusmod tempor incididunt ut labore et dolore magna aliqua. Quis ipsum suspendisse</p><a class="more">READ MORE ⟶</a></article>

<section class="section news">
  <h3>SUBSCRIBE TO OUR NEWSLETTER</h3>
  <p>A short sentence describing what someone will receive by subscribing</p>
  <div class="news-form"><span>Enter Your Email Address</span><span class="btn-solid">Subscribe</span></div>
</section>

<footer class="section footer">
  <div class="fcol" style="left:120px"><h6>Quick Links</h6><ul><li>Search</li><li>Become a Seller</li><li>Contact Us</li><li>Refund Policy</li><li>Shipping Policy</li><li>Privacy Policy</li><li>Terms of Service</li></ul></div>
  <div class="fcol" style="left:310px"><h6>Main Menu</h6><ul><li>Home</li><li>About Us</li><li>Shop</li><li>Blog</li><li>Contact &amp; FAQ</li><li>Press &amp; Awards</li></ul></div>
  <div class="fcol" style="left:500px;width:360px"><h6>Purchasing &amp;Distribution</h6><p>Lorem ipsum dolor sit amet, consectetur adipiscing elit, sed do eiusmod tempor incididunt ut labore et dolore magna aliqua. Quis ipsum suspendisse ultrices</p><p>✉ info@brightwelllights.com</p><p>☎ 1-555-010-2040</p><p>⚲ 48 Lantern Way, Springfield USA 20410</p></div>
  <div class="fcol" style="left:882px;width:210px"><h6>News &amp; Updates</h6><p>Sign up to get the latest on sales, new releases and more ...</p><div class="femail"><span>Enter you email</span><i></i></div><div class="social" aria-label="Social links"><i></i><i></i><i></i><i></i></div></div>
  <div class="copy">Copyright © 2021 Brightwell Lights. All Rights Reserved.</div>
  <div class="pay"><span><i></i>Northpay</span><span><i></i>Cardwell</span><span><i></i>Tradex</span><span><i></i>Pocketpay</span><span><i></i>Tapwise</span></div>
</footer>

</body>
</html>
```